DeSIGN OF CARDS AND STATIONARY
MIRELLO VANTURA LAW
DeSIGN OF CARDS AND STATIONARY - Law
Creative Brief
Cutting-Edge
Rosalind Mirello Vantura
Criminal ATTORNEY
no address on the. card
rosalind@mirellovanturalaw.example
www.mirellovanturalaw.example
I. already. have. a logo I want to use
front of the. card will be the logo and name I send you. and in the back of the card will be. my info with logo. NEED TO ATTACH THE LOGO I JUST GOT.

```html
<!DOCTYPE html>
<html lang="en">
<head>
<meta charset="utf-8">
<title>Mirello Vantura Law – Business Cards</title>
<link href="https://fonts.googleapis.com/css2?family=Montserrat:wght@400&family=Roboto+Slab:wght@400;700&display=swap" rel="stylesheet">
<style>
  :root {
    --backdrop: #2a2a2d;
    --navy: #1b1e58;
    --steel-blue: #5a7db0;
    --logo-tint: #c9d2e6;
    --logo-ink: #2a2f66;
    --paper: #ffffff;
    --text-light: #ffffff;
    --text-soft: #c8cde3;
  }
  * { margin: 0; padding: 0; box-sizing: border-box; }
  html, body {
    width: 1200px; height: 871px; overflow: hidden;
    background: var(--backdrop);
  }
  .stage {
    position: relative; width: 1200px; height: 871px;
    display: flex; align-items: center; justify-content: center; gap: 40px;
  }
  .card {
    position: relative; width: 540px; height: 309px; overflow: hidden;
    box-shadow: 0 12px 30px rgba(0,0,0,0.45);
  }
  /* Front */
  .card-front {
    background: var(--navy);
    display: flex; flex-direction: column; align-items: center; justify-content: center;
  }
  .brand {
    display: flex; flex-direction: column; align-items: center; gap: 14px;
    font-family: "Montserrat", sans-serif; font-weight: 400;
  }
  .brand-dot {
    width: 34px; height: 34px; border-radius: 50%;
    background: var(--steel-blue);
  }
  .brand-name {
    font-size: 19px; letter-spacing: 5px; text-align: center; line-height: 1.5;
    white-space: nowrap;
  }
  .card-front .brand-name { color: var(--logo-tint); }
  /* Back */
  .card-back { background: var(--paper); }
  .card-back .swoosh { position: absolute; inset: 0; }
  .card-back .brand {
    position: absolute; left: 30px; top: 92px; width: 150px; gap: 12px;
  }
  .card-back .brand-dot { width: 26px; height: 26px; }
  .card-back .brand-name { color: var(--logo-ink); font-size: 14px; letter-spacing: 3px; line-height: 1.55; }
  .contact-block {
    position: absolute; left: 290px; top: 104px;
    font-family: "Roboto Slab", serif; color: var(--text-light);
  }
  .person-name { font-size: 17px; font-weight: 700; white-space: nowrap; }
  .person-role { font-size: 10.5px; color: var(--text-soft); margin-top: 5px; }
  .contact-list { list-style: none; margin-top: 20px; }
  .contact-list li {
    display: flex; align-items: center; gap: 7px; white-space: nowrap;
    font-size: 10px; color: var(--text-soft); margin-bottom: 5px;
  }
  .contact-list svg { width: 9px; height: 9px; fill: var(--text-light); flex: none; }
</style>
</head>
<body>
<main class="stage">
  <section class="card card-front" aria-label="Card front">
    <div class="brand">
      <span class="brand-dot"></span>
      <div class="brand-name">MIRELLO VANTURA<br>LAW</div>
    </div>
  </section>

  <section class="card card-back" aria-label="Card back">
    <svg class="swoosh" viewBox="0 0 540 309" preserveAspectRatio="none" aria-hidden="true">
      <path d="M98 309 C 138 200, 228 70, 458 0 L540 0 L540 309 Z" fill="var(--steel-blue)"/>
      <path d="M120 309 C 160 200, 250 70, 480 0 L540 0 L540 309 Z" fill="var(--navy)"/>
    </svg>
    <div class="brand">
      <span class="brand-dot"></span>
      <div class="brand-name">MIRELLO<br>VANTURA<br>LAW</div>
    </div>
    <div class="contact-block">
      <div class="person-name">Rosalind Mirello Vantura</div>
      <div class="person-role">Criminal ATTORNEY</div>
      <ul class="contact-list">
        <li>
          <svg viewBox="0 0 10 10" aria-hidden="true"><path d="M2 0.5 L3.6 0.5 L4.2 3 L3 3.8 C3.6 5.2 4.8 6.4 6.2 7 L7 5.8 L9.5 6.4 L9.5 8 C9.5 9 8.8 9.5 8 9.5 C3.8 9.2 0.8 6.2 0.5 2 C0.5 1.2 1 0.5 2 0.5 Z"/></svg>
          305-555-0147
        </li>
        <li>
          <svg viewBox="0 0 10 10" aria-hidden="true"><path d="M0.5 2 H9.5 V8 H0.5 Z M0.5 2 L5 5.5 L9.5 2" stroke="var(--navy)" stroke-width="0.8"/></svg>
          rosalind@mirellovanturalaw.example
        </li>
        <li>
          <svg viewBox="0 0 10 10" aria-hidden="true"><circle cx="5" cy="5" r="4.5"/><path d="M0.5 5 H9.5 M5 0.5 C2.5 3 2.5 7 5 9.5 M5 0.5 C7.5 3 7.5 7 5 9.5" stroke="var(--navy)" stroke-width="0.7" fill="none"/></svg>
          www.mirellovanturalaw.example
        </li>
      </ul>
    </div>
  </section>
</main>
</body>
</html>
```